Investment company seeks website design

KRV (Halvorsen Capital Partners) are an investment company that actively targets and acquires businesses and grows them after acquisition.

The website design needs to be professional and should communicate to key decision-makers inside the acquirable companies that KRV targets.

You will design the Homepage initially for the competition. If you win the competition, you will design the inner pages too.

More details are attached below.

Target Market(s)

Business owners and decision makers inside acquirable companies

Industry/Entity Type

Company Investment

Number of Pages Required

5+ page

Requirements
Must have
• High Attention to Detail. Following the Wireframes closely. Consistent colour and design choices
Should not have
• Anything cheap, too bright or untidy

```html
<!DOCTYPE html>
<html lang="en">
<head>
<meta charset="utf-8">
<title>Halvorsen Capital Partners — Home</title>
<link href="https://fonts.googleapis.com/css2?family=Questrial&family=Roboto:wght@400;500;700&display=swap" rel="stylesheet">
<style>
:root{
  --navy:#1d2f5a;
  --navy-deep:#13244a;
  --green:#76b843;
  --grey-btn:#9a9696;
  --light:#edf2f9;
  --text:#5d6470;
  --muted:#9aa0a8;
  --white:#fff;
}
*{box-sizing:border-box;margin:0;padding:0}
html,body{width:1200px;height:3881px;overflow:hidden}
body{font-family:"Roboto",sans-serif;color:var(--text);background:var(--white);position:relative}
.abs{position:absolute}
.heading{font-family:"Questrial",sans-serif;color:var(--navy);text-transform:uppercase;font-weight:400}
.btn{position:absolute;background:var(--grey-btn);color:#fff;font:500 12px "Roboto",sans-serif;text-transform:uppercase;display:flex;align-items:center;justify-content:center;letter-spacing:.2px}

/* header */
.site-header{position:absolute;left:0;top:0;width:1200px;height:78px;border-top:4px solid var(--green);background:#fff}
.brand{position:absolute;left:145px;top:18px;display:flex;align-items:center;gap:12px}
.brand-mark{width:30px;height:30px;background:var(--navy)}
.brand-name{font:400 22px "Questrial",sans-serif;color:var(--navy)}
.nav{position:absolute;left:480px;top:31px;display:flex;gap:28px;font:500 12px "Roboto",sans-serif;color:var(--navy-deep);text-transform:uppercase}
.nav a:first-child{border-left:3px solid var(--green);padding-left:4px}
.nav a{color:inherit;text-decoration:none}
.nav-cta{left:970px;top:26px;width:86px;height:31px}

/* hero */
.hero{position:absolute;left:0;top:78px;width:1200px;height:522px}
.hero-title{position:absolute;font:400 38px/45px "Questrial",sans-serif;color:#fff;text-transform:uppercase}
.hero-title .accent{color:var(--green)}
.hero-cta{left:525px;top:240px;width:150px;height:40px;border:3px solid #e3e3e3}

/* about */
.about-title{left:143px;top:672px;font-size:40px;line-height:46px}
.about-copy{left:143px;top:825px;width:415px;font-size:13px;line-height:24px;text-align:justify;color:#6b7079}
.about-cta{left:143px;top:1072px;width:207px;height:32px}
.about-frame{left:621px;top:665px;width:435px;height:475px;border:1px solid #cfd3d8;background:#fff}

/* qualities */
.qualities{position:absolute;left:0;top:1218px;width:1200px;height:632px;background:var(--light)}
.section-title{position:absolute;left:0;width:1200px;text-align:center;font-size:38px;line-height:46px}
.quality{position:absolute;width:470px;height:190px}
.quality svg{position:absolute;left:0;top:0}
.quality-body{position:absolute;left:190px;top:38px}
.quality h3{font:500 14px "Roboto",sans-serif;color:var(--navy-deep);text-transform:uppercase;margin-bottom:8px}
.quality li{list-style:none;font-size:12.5px;line-height:21.5px;color:#6b7079;padding-left:19px;position:relative}
.quality li::before{content:"";position:absolute;left:1px;top:8px;width:7px;height:7px;border-radius:50%;background:var(--green)}

/* explore */
.explore{position:absolute;left:0;top:1850px;width:1200px;height:444px;background:radial-gradient(ellipse at 60% 70%,#1e4a8a 0%,#13306a 40%,#0c1c3c 100%)}
.explore-title{position:absolute;left:0;width:1200px;top:140px;text-align:center;font:400 38px "Questrial",sans-serif;color:#fff;text-transform:uppercase}
.explore-sub{position:absolute;left:0;width:1200px;top:207px;text-align:center;font-size:14px;color:#fff}
.explore-cta{left:497px;top:262px;width:206px;height:34px}

/* transform */
.step{position:absolute;width:310px;height:310px;border-radius:50%;border:4px solid var(--navy);background:#fff;text-align:center}
.step.featured{border:7px solid var(--green)}
.step svg{margin-top:42px}
.step h3{font:500 14.5px/21px "Roboto",sans-serif;color:var(--navy-deep);text-transform:uppercase;margin-top:12px}
.step p{font-size:13.5px;line-height:21px;color:var(--muted);margin:12px auto 0;width:210px}
.divider{position:absolute;left:150px;top:2893px;width:900px;height:1px;background:#eceef1}

/* news */
.news-card{position:absolute;top:3035px;width:295px;height:193px;background:#fff;box-shadow:0 1px 5px rgba(0,0,0,.18);padding:22px 16px 0}
.news-card h3{font:400 16px/24px "Roboto",sans-serif;color:#2a2f38}
.news-card p{font-size:11px;line-height:21px;color:var(--muted);margin-top:10px;padding-bottom:12px;border-bottom:1px solid #eceef1}
.news-meta{display:flex;align-items:center;gap:6px;font-size:10.5px;color:#777;margin-top:14px}
.news-meta span{margin-right:10px}
.arrow{position:absolute;top:3122px}

/* cta band */
.cta-band{position:absolute;left:0;top:3295px;width:1200px;height:270px;background:linear-gradient(90deg,#eef0f2 0%,#e8ebee 55%,#cfd8e3 75%,#6f86a6 100%)}
.cta-title{left:143px;top:85px;font-size:31px;line-height:39px}

/* footer */
.footer-links{position:absolute;left:196px;top:3624px;display:flex;flex-direction:column;gap:14px;font-size:15.5px;color:#2a2f38}
.footer-col{position:absolute;top:3620px;font-size:15.5px;color:#2a2f38;line-height:30px}
.footer-col h4{font:500 21px "Roboto",sans-serif;color:var(--navy);text-transform:uppercase;margin-bottom:4px}
.footer-btn{position:relative;width:100px;height:34px;margin-top:6px;font-size:14px;text-transform:uppercase}
.footer-bottom{position:absolute;left:0;top:3795px;width:1200px;border-top:1px solid #dfe2e6;text-align:center;padding-top:35px;font-size:13.5px;color:#2a2f38}
</style>
</head>
<body>

<header class="site-header">
  <div class="brand"><span class="brand-mark"></span><span class="brand-name">Halvorsen Capital Partners</span></div>
  <nav class="nav"><a href="#">Our Approach</a><a href="#">Investment Criteria</a><a href="#">About Us</a><a href="#">Contact Us</a></nav>
  <div class="btn nav-cta">Email Us</div>
</header>

<section class="hero">
  <svg width="1200" height="522" viewBox="0 0 1200 522">
    <defs>
      <linearGradient id="heroNavy" x1="0" y1="0" x2="1" y2="1"><stop offset="0" stop-color="#1d2f5a"/><stop offset=".6" stop-color="#2a437a"/><stop offset="1" stop-color="#1a2b55"/></linearGradient>
      <linearGradient id="heroGreen" x1="0" y1="0" x2="1" y2="1"><stop offset="0" stop-color="#6fae3f"/><stop offset=".5" stop-color="#7fbd4a"/><stop offset="1" stop-color="#5f9f36"/></linearGradient>
    </defs>
    <polygon points="0,0 525,0 720,522 0,522" fill="url(#heroNavy)" role="img" aria-label="Hand reaching toward a rising financial chart, navy toned"/>
    <polygon points="545,0 1200,0 1200,522 740,522" fill="url(#heroGreen)" role="img" aria-label="Smiling business team working at laptops, green toned"/>
  </svg>
  <h1 class="hero-title" style="left:143px;top:182px"><span class="accent">The Best</span> Exit<br>For You</h1>
  <h2 class="hero-title" style="left:702px;top:182px">The Best Future<br>For Your<br>Business</h2>
  <div class="btn hero-cta">Discover KRV</div>
</section>

<h2 class="heading abs about-title">We Will Make<br>Your Business<br>Thrive</h2>
<p class="abs about-copy">Sed ut perspiciatis unde omnis iste natus error sit voluptatem accusantium doloremque laudantium, totam rem aperiam, eaque ipsa quae ab illo inventore veritatis et quasi architecto beatae vitae dicta sunt explicabo. Nemo enim ipsam voluptatem quia voluptas sit aspernatur aut odit aut fugit, sed quia consequuntur magni dolores eos qui ratione voluptatem sequi nesciunt. Neque porro quisquam est, qui dolorem ipsum quia dolor sit amet, consectetur, adipisci velit, sed quia non numquam eius modi tempora incidunt ut labore et dolore magnam aliquam quaerat voluptatem</p>
<div class="btn about-cta">Unlock Your Potential</div>
<div class="abs about-frame">
  <div class="abs" style="left:222px;top:0;width:213px;height:153px;background:var(--green)"></div>
  <div class="abs" style="left:0;top:320px;width:213px;height:155px;background:var(--navy)"></div>
  <div class="abs" style="left:16px;top:17px;width:398px;height:438px;background:#fff"></div>
  <div class="abs" role="img" aria-label="Businessman writing notes at a desk beside a laptop" style="left:24px;top:26px;width:384px;height:420px;background:linear-gradient(135deg,#c9d5e3 0%,#a9b9cc 45%,#8e7f6c 100%)"></div>
</div>

<section class="qualities">
  <h2 class="heading section-title" style="top:68px">Our Qualities &amp; Capabilities</h2>

  <div class="quality" style="left:160px;top:152px">
    <svg width="165" height="187"><polygon points="82.5,0 165,46.75 165,140.25 82.5,187 0,140.25 0,46.75" fill="#3c5b86" role="img" aria-label="Hand holding a tablet showing financial charts"/></svg>
    <div class="quality-body"><h3>Driving Value</h3><ul><li>Sed ut perspiciatis u omnis iste</li><li>Natus error sit voluptatem</li><li>Accusantium doloaudantium,</li><li>Totam rem aperique ipsa quae</li></ul></div>
  </div>
  <div class="quality" style="left:640px;top:152px">
    <svg width="165" height="187"><polygon points="82.5,0 165,46.75 165,140.25 82.5,187 0,140.25 0,46.75" fill="#7a5f4c" role="img" aria-label="Team hands joining colourful puzzle pieces on a table"/></svg>
    <div class="quality-body"><h3>Integrated Team</h3><ul><li>Sed ut perspiciatis u omnis iste</li><li>Natus error sit voluptatem</li><li>Accusantium doloaudantium,</li><li>Totam rem aperique ipsa quae</li></ul></div>
  </div>
  <div class="quality" style="left:160px;top:368px">
    <svg width="165" height="187"><polygon points="82.5,0 165,46.75 165,140.25 82.5,187 0,140.25 0,46.75" fill="#b9c2cc" role="img" aria-label="Business colleagues shaking hands in a meeting"/></svg>
    <div class="quality-body"><h3>Partnership With Management</h3><ul><li>Sed ut perspiciatis u omnis iste</li><li>Natus error sit voluptatem</li><li>Accusantium doloaudantium,</li><li>Totam rem aperique ipsa quae</li></ul></div>
  </div>
  <div class="quality" style="left:640px;top:368px">
    <svg width="165" height="187"><polygon points="82.5,0 165,46.75 165,140.25 82.5,187 0,140.25 0,46.75" fill="#9fb0c6" role="img" aria-label="Hands reviewing printed financial charts with a pen"/></svg>
    <div class="quality-body"><h3>Accelerated Execution</h3><ul><li>Sed ut perspiciatis u omnis iste</li><li>Natus error sit voluptatem</li><li>Accusantium doloaudantium,</li><li>Totam rem aperique ipsa quae</li></ul></div>
  </div>
</section>

<section class="explore" role="img" aria-label="Glowing blue stock market bar chart background">
  <h2 class="explore-title">Explore Your Next Move</h2>
  <p class="explore-sub">Sed ut perspiciatis unde omnis iste natus error sit voluptatem accusantium</p>
  <div class="btn explore-cta">Unlock Your Potential</div>
</section>

<h2 class="heading section-title" style="top:2382px;font-size:39px;line-height:46px">How KRV Will Transform<br>Your Company</h2>

<div class="step" style="left:143px;top:2518px">
  <svg width="72" height="70" viewBox="0 0 72 70" fill="none" stroke="#76b843" stroke-width="2.5"><path d="M6 64h60"/><rect x="10" y="44" width="8" height="20"/><rect x="24" y="36" width="8" height="28"/><rect x="38" y="28" width="8" height="36"/><rect x="52" y="20" width="8" height="44"/><path d="M8 36 L30 20 L40 26 L60 8"/><path d="M50 8h10v10"/></svg>
  <h3>Discover Growth<br>Opportunities</h3>
  <p>Sed ut perspiciatis unde omnis iste natus error sit volupt atem accusantium</p>
</div>
<div class="step featured" style="left:441px;top:2515px;width:318px;height:318px">
  <svg width="72" height="70" viewBox="0 0 72 70" fill="none" stroke="#76b843" stroke-width="2.5"><rect x="8" y="14" width="56" height="42"/><path d="M8 56l-4 10M64 56l4 10M36 6v8"/><path d="M16 46 L28 34 L38 40 L54 24"/><circle cx="30" cy="26" r="6"/></svg>
  <h3>Craft Strategic<br>Solutions</h3>
  <p>Sed ut perspiciatis unde omnis iste natus error sit volupt atem accusantium</p>
</div>
<div class="step" style="left:745px;top:2518px">
  <svg width="72" height="70" viewBox="0 0 72 70" fill="none" stroke="#76b843" stroke-width="2.5"><circle cx="18" cy="52" r="9"/><circle cx="18" cy="52" r="3"/><path d="M28 56 L62 22"/><path d="M50 20h12v12"/><path d="M56 4l2 5 5 1-4 3 1 5-4-3-4 3 1-5-4-3 5-1z"/><path d="M12 10l2 4M20 6l-1 5"/></svg>
  <h3>Drive Future<br>Success</h3>
  <p>Sed ut perspiciatis unde omnis iste natus error sit volupt atem accusantium</p>
</div>

<div class="divider"></div>

<h2 class="heading section-title" style="top:2953px;font-size:39px">KRV News &amp; Insights</h2>

<svg class="arrow" style="left:103px" width="22" height="16" viewBox="0 0 22 16" fill="none" stroke="#777" stroke-width="2"><path d="M21 8H2M9 1L2 8l7 7"/></svg>
<svg class="arrow" style="left:1075px" width="22" height="16" viewBox="0 0 22 16" fill="none" stroke="#777" stroke-width="2"><path d="M1 8h19M13 1l7 7-7 7"/></svg>

<article class="news-card" style="left:145px">
  <h3>Sed ut perspiciatis unde omnis iste natus error sit ..</h3>
  <p>Lorem ipsum dolor sit amet, consectetur adipiscing elitsed do eiusmod tempor..</p>
  <div class="news-meta"><svg width="10" height="11" viewBox="0 0 10 11" fill="none" stroke="#76b843"><circle cx="5" cy="3.5" r="2.5"/><path d="M1 10.5c0-3 8-3 8 0"/></svg><span>By Admin</span><svg width="11" height="10" viewBox="0 0 11 10" fill="none" stroke="#76b843"><rect x=".5" y="1.5" width="10" height="8"/><path d="M.5 4h10"/></svg><span>November 10 , 2017</span></div>
</article>
<article class="news-card" style="left:452px">
  <h3>Sed ut perspiciatis unde omnis iste natus error sit ..</h3>
  <p>Lorem ipsum dolor sit amet, consectetur adipiscing elitsed do eiusmod tempor..</p>
  <div class="news-meta"><svg width="10" height="11" viewBox="0 0 10 11" fill="none" stroke="#76b843"><circle cx="5" cy="3.5" r="2.5"/><path d="M1 10.5c0-3 8-3 8 0"/></svg><span>By Admin</span><svg width="11" height="10" viewBox="0 0 11 10" fill="none" stroke="#76b843"><rect x=".5" y="1.5" width="10" height="8"/><path d="M.5 4h10"/></svg><span>November 10 , 2017</span></div>
</article>
<article class="news-card" style="left:760px">
  <h3>Sed ut perspiciatis unde omnis iste natus error sit ..</h3>
  <p>Lorem ipsum dolor sit amet, consectetur adipiscing elitsed do eiusmod tempor..</p>
  <div class="news-meta"><svg width="10" height="11" viewBox="0 0 10 11" fill="none" stroke="#76b843"><circle cx="5" cy="3.5" r="2.5"/><path d="M1 10.5c0-3 8-3 8 0"/></svg><span>By Admin</span><svg width="11" height="10" viewBox="0 0 11 10" fill="none" stroke="#76b843"><rect x=".5" y="1.5" width="10" height="8"/><path d="M.5 4h10"/></svg><span>November 10 , 2017</span></div>
</article>

<section class="cta-band">
  <div class="abs" role="img" aria-label="Hand touching a digital business analytics interface" style="left:680px;top:0;width:520px;height:270px;background:linear-gradient(90deg,rgba(232,235,238,0) 0%,rgba(160,178,204,.6) 50%,#5b7397 100%)"></div>
  <h2 class="heading abs cta-title">Sed ut perspiciatis unde<br>omnis iste natus error sit<br>voluptatem accusantium</h2>
  <svg class="abs" style="left:750px;top:40px" width="400" height="200" viewBox="0 0 400 200" font-family="Roboto,sans-serif" font-size="10" font-weight="500" text-anchor="middle">
    <polygon points="50,6 88,28 88,72 50,94 12,72 12,28" fill="#fff" stroke="#76b843" stroke-width="7"/><text x="50" y="54" fill="#1d2f5a">Finance</text>
    <polygon points="346,6 384,28 384,72 346,94 308,72 308,28" fill="#fff" stroke="#1d2f5a" stroke-width="7"/><text x="346" y="54" fill="#1d2f5a">Strategy</text>
    <polygon points="101,100 139,122 139,166 101,188 63,166 63,122" fill="#fff" stroke="#1d2f5a" stroke-width="7"/><text x="101" y="148" fill="#1d2f5a" font-size="9.5">Partnerships</text>
    <polygon points="280,100 318,122 318,166 280,188 242,166 242,122" fill="#fff" stroke="#76b843" stroke-width="7"/><text x="280" y="148" fill="#1d2f5a" font-size="9.5">Operations</text>
  </svg>
</section>

<nav class="footer-links"><span>Our Approach</span><span>Investment Criteria</span><span>About Us</span><span>Contact Us</span></nav>
<div class="footer-col" style="left:456px">
  <h4>Our Team</h4>
  <div>+44(0)7700 900123</div>
  <div class="btn footer-btn">Email Us</div>
</div>
<div class="footer-col" style="left:745px">
  <h4>Address</h4>
  <div>Halvorsen Capital Partners<br>Sed ut perspiciatis unde omnis iste<br>natus error sit voccusantium</div>
</div>
<footer class="footer-bottom">© 2024 Halvorsen Capital Partners . All rights reserved.Privacy &nbsp;|&nbsp; Terms of Use</footer>

</body>
</html>
```